Orbell Consulting- executive coaching business

looking for business card design for a newly started coaching business.
specialising in Exective coaching, Leadership, NLP and Motivation.
Looking for a simple, classy design using the existing logo attached and colour themes that complement the logo.
No red or orange in the business card design please.

Target Market(s)

Defence and Veteran community

Industry/Entity Type

Life Coaching

Contact Information for Business Card

looking for business cards for newly started coaching business.
specialising in Exective Coaching, Leadership, NLP and Motivation

Font styles to use
Serif
Script

Colors
0556a4
3176b5
86cfc6
33b8a4

Requirements
Must have
• Logo
• Email address- Jess@orbellconsulting.com.au
• Contact number
• Services provided - Executive Coaching, Leadership, NLP and Motivational Mapping.
Nice to have
• Same colours as logo
Should not have
• Red or orange

```html
<!DOCTYPE html>
<html lang="en">
<head>
<meta charset="utf-8">
<title>Orbell Consulting – Business Card</title>
<link rel="stylesheet" href="https://fonts.googleapis.com/css2?family=Open+Sans:wght@400;600;700&display=swap">
<style>
  :root {
    --page-bg: #e9ecef;
    --card-white: #ffffff;
    --brand-blue: #0556a4;
    --blue-light: #1f8fd8;
    --blue-mid: #0f74c0;
    --blue-deep: #0a5fa8;
    --text-on-blue: #ffffff;
    --rule-green: #33b8a4;
  }
  * { box-sizing: border-box; margin: 0; padding: 0; }
  html, body {
    width: 1200px; height: 950px; overflow: hidden;
    background: var(--page-bg);
    font-family: "Open Sans", Arial, sans-serif;
  }
  .canvas {
    width: 1200px; height: 950px;
    display: flex; flex-direction: column;
    align-items: center; justify-content: center; gap: 50px;
  }
  .card {
    width: 700px; height: 400px;
    border-radius: 22px;
    position: relative; overflow: hidden;
    box-shadow: 0 8px 24px rgba(0,0,0,0.18);
  }
  /* Front */
  .card-front {
    background: var(--card-white);
    display: flex; align-items: center; justify-content: center;
  }
  .brand-lockup { display: flex; align-items: center; gap: 16px; }
  .brand-dot {
    width: 46px; height: 46px; border-radius: 50%;
    border: 3px solid var(--brand-blue);
  }
  .brand-name {
    font-weight: 700; font-size: 40px; letter-spacing: 0.5px;
    color: var(--brand-blue); text-transform: uppercase;
  }
  /* Back */
  .card-back {
    background: linear-gradient(135deg, var(--blue-light) 0%, var(--blue-mid) 55%, var(--blue-deep) 100%);
    color: var(--text-on-blue);
  }
  .back-ring { position: absolute; left: -40px; top: 95px; }
  .back-details {
    position: absolute; right: 42px; top: 34px;
    text-align: right; line-height: 1.35;
  }
  .person-name { font-weight: 700; font-size: 22px; }
  .person-role, .contact-line { font-size: 15px; }
  .person-role { margin-bottom: 4px; }
  .services-heading { font-weight: 700; font-size: 19px; margin-top: 10px; }
  .services-list { list-style: none; font-size: 15px; }
  .services-list li::after { content: " \2022"; font-weight: 700; }
  .back-brand {
    position: absolute; right: 42px; bottom: 44px; text-align: right;
  }
  .back-brand .brand-name { color: var(--text-on-blue); font-size: 32px; }
  .brand-rule {
    display: block; margin-left: auto; margin-top: 6px;
    width: 300px; height: 2px; background: var(--text-on-blue);
  }
</style>
</head>
<body>
<main class="canvas">
  <section class="card card-front" aria-label="Business card front">
    <div class="brand-lockup">
      <span class="brand-dot" aria-hidden="true"></span>
      <span class="brand-name">Orbell Consulting</span>
    </div>
  </section>

  <section class="card card-back" aria-label="Business card back">
    <svg class="back-ring" width="360" height="360" viewBox="0 0 360 360" aria-hidden="true">
      <circle cx="180" cy="180" r="168" fill="none" stroke="var(--text-on-blue)" stroke-width="9"/>
    </svg>

    <div class="back-details">
      <p class="person-name">Daniel Hart</p>
      <p class="person-role">CEO/Founder</p>
      <p class="contact-line">612 555 0148</p>
      <p class="contact-line">Jess@orbellconsulting.com.au</p>
      <p class="contact-line">www.orbellconsulting.com.au</p>
      <p class="services-heading">Services provided</p>
      <ul class="services-list">
        <li>Executive Coaching</li>
        <li>Leadership</li>
        <li>NLP &amp; Motivational Mapping</li>
      </ul>
    </div>

    <div class="back-brand">
      <span class="brand-name">Orbell Consulting</span>
      <span class="brand-rule" aria-hidden="true"></span>
    </div>
  </section>
</main>
</body>
</html>
```